Freelance business trainer needs a new business card

My business is called Tbrite. I provide training in the workplace on management, coaching and mentoring, and customer service topics for a variety of businesses, colleges and private training providers, and teach on management programs. I need a professional but eye catching business card. Business colours grey and orange. My name Linda Marchbank; Tel 07853 416207; email lmarchbank@tbrite.co.uk; website www.tbrite.co.uk.
Happy to have some sort of logo on front and details on back or all on one side
Target Market(s)
SME businesses and colleges - workshops i run are for adults in the workplace
Industry/Entity Type
Training
Look and feel

```html
<!DOCTYPE html>
<html lang="en">
<head>
<meta charset="utf-8">
<title>Tbrite business card</title>
<link rel="stylesheet" href="https://fonts.googleapis.com/css2?family=PT+Sans+Narrow:wght@400;700&display=swap">
<style>
  :root {
    --page: #e9e6e2;
    --white: #ffffff;
    --orange: #f07d1a;
    --orange-light: #f9b24c;
    --orange-deep: #ea5d14;
    --grey-light: #8d8e90;
    --grey-mid: #606164;
    --grey-dark: #3a3b3d;
    --shadow: rgba(0, 0, 0, 0.28);
  }
  * { margin: 0; padding: 0; box-sizing: border-box; }
  html, body {
    width: 1200px;
    height: 913px;
    overflow: hidden;
    background: var(--page);
    font-family: "PT Sans Narrow", "Arial Narrow", sans-serif;
  }
  .canvas { position: relative; width: 1200px; height: 913px; }

  .card {
    position: absolute;
    width: 560px;
    height: 320px;
    overflow: hidden;
    box-shadow: 0 10px 26px var(--shadow);
  }

  /* Front */
  .card-front { left: 70px; top: 90px; background: var(--white); }
  .card-front .upper { position: absolute; inset: 0 0 auto 0; height: 150px; background: var(--white); }
  .card-front .divider { position: absolute; left: 0; right: 0; top: 150px; height: 3px; background: var(--orange); }
  .card-front .lower {
    position: absolute; left: 0; right: 0; top: 153px; bottom: 0;
    background: linear-gradient(160deg, var(--grey-light) 0%, var(--grey-mid) 45%, var(--grey-dark) 100%);
  }
  .brand {
    position: absolute; left: 34px; top: 76px;
    font-weight: 700; font-size: 40px; line-height: 1;
    color: var(--grey-mid);
  }
  .person-name {
    position: absolute; left: 34px; bottom: 52px;
    font-size: 27px; color: var(--orange); font-weight: 400;
  }
  .contact { position: absolute; left: 300px; top: 170px; list-style: none; }
  .contact li {
    display: flex; align-items: center; gap: 8px;
    color: var(--white); font-size: 16px; font-weight: 700; line-height: 24px;
    white-space: nowrap;
  }
  .contact svg { width: 14px; height: 14px; flex: none; }
  .contact .address { font-size: 12.5px; padding-left: 22px; }

  /* Back */
  .card-back {
    left: 570px; top: 500px;
    background: linear-gradient(170deg, var(--grey-light) 0%, var(--grey-mid) 50%, var(--grey-dark) 100%);
  }
  .card-back .band {
    position: absolute; left: 0; right: 0; top: 100px; height: 115px;
    background: linear-gradient(30deg, var(--orange-deep) 0%, var(--orange) 45%, var(--orange-light) 100%);
    display: flex; align-items: center; justify-content: center;
  }
  .band-name { font-weight: 700; font-size: 56px; color: var(--white); }
</style>
</head>
<body>
<main class="canvas">

  <section class="card card-front" aria-label="Business card front">
    <div class="upper"></div>
    <div class="divider"></div>
    <div class="lower"></div>

    <div class="brand">Tbrite</div>

    <ul class="contact">
      <li>
        <svg viewBox="0 0 14 14" aria-hidden="true"><path d="M3 1 L5.5 3.5 L4 5.5 Q5.5 8.5 8.5 10 L10.5 8.5 L13 11 L11 13 Q4 12 1 3 Z" fill="var(--orange)"/></svg>
        07853 416207
      </li>
      <li>
        <svg viewBox="0 0 14 14" aria-hidden="true"><rect x="1" y="3" width="12" height="8" fill="var(--orange)"/><path d="M1 3 L7 8 L13 3" stroke="var(--grey-mid)" stroke-width="1.2" fill="none"/></svg>
        lmarchbank@tbrite.co.uk
      </li>
      <li>
        <svg viewBox="0 0 14 14" aria-hidden="true"><path d="M6 4 H4 a3 3 0 0 0 0 6 H6 M8 4 H10 a3 3 0 0 1 0 6 H8 M4.5 7 H9.5" stroke="var(--orange)" stroke-width="1.8" fill="none"/></svg>
        www.tbrite.co.uk
      </li>
      <li class="address">Willow House Farley Lane Ashby RG31 4TN</li>
    </ul>

    <div class="person-name">Linda Marchbank</div>
  </section>

  <section class="card card-back" aria-label="Business card back">
    <div class="band">
      <span class="band-name">Tbrite</span>
    </div>
  </section>

</main>
</body>
</html>
```